Business Card Design Project

Use newly designed logo and tie into newly designed website
I need a new logo and website layout designed for my partner's business. This is a birthday present. His business is interior painting, wallpapering and design. He also has access to a wide variety of products including carpet, fabrics, furniture, wallpaper, tile, countertops, etc. I have attached some screen shots of his website for reference. He is a one man shop and has a stellar reputation with his customers. He is on-time, very tidy, excellent with animals, and always finishes on time and on budget. There are no restrictions on colors or fonts. The logo needs to work well with the website, business cards and printed materials. The website needs to flow content for device size so it looks just as good on a cell phone or tablet as it does on a desktop computer. Whatever the heck that's called!Thanks. I am looking forward to seeing everyone's ideas.
Updates
Hi Designers,
We've reopened this project as our logo design project has just completed.
Please refer to the uploaded files and make use of either Horizontal or Vertical versions of the logo depending on what you think is suitable for your design proposals.
We look forward to your creative submissions!
Target Market(s)
Consumers looking to improve the interior environment of their homes by updating wall paint or paper, flooring (either carpet, tile, or hardwoods), counter tops, window treatments, etc. Clients tend to be more upper middle class and have certain taste levels and expectations. New logo, website and business card should align to meet those levels.
Industry/Entity Type
Cell Phone
Look and feel
Each slider illustrates characteristics of the customer's brand and the style your logo design should communicate.

```html
<!DOCTYPE html>
<html lang="en">
<head>
<meta charset="utf-8">
<title>Marlow Interior Designs — Business Cards</title>
<link rel="stylesheet" href="https://fonts.googleapis.com/css2?family=Cinzel:wght@400;600&display=swap">
<style>
  :root{
    --navy:#1e1440;
    --orange:#f7931e;
    --tan:#a68d5f;
    --maroon:#7a1e22;
    --paper:#ffffff;
    --backdrop:#e6e3de;
    --serif:'Cinzel', Georgia, serif;
  }
  *{box-sizing:border-box;margin:0;padding:0}
  html,body{width:1200px;height:1000px;overflow:hidden}
  body{background:var(--backdrop);font-family:var(--serif);position:relative;color:var(--navy)}

  .card{position:absolute;background:var(--paper);box-shadow:0 2px 10px rgba(0,0,0,.12);overflow:hidden}
  .card--horizontal{width:380px;height:217px;border-radius:14px}

  /* Vertical arch card */
  .card--arch{left:108px;top:195px;width:362px;height:607px;border-radius:181px 181px 0 0}
  .arch__mark{position:absolute;left:85px;top:80px;width:192px;height:192px;background:var(--navy)}
  .arch__brand{position:absolute;left:0;right:0;top:272px;text-align:center;color:var(--navy);font-weight:600}
  .arch__brand .brand-main{display:block;font-size:38px;line-height:44px;letter-spacing:1px}
  .arch__brand .brand-sub{display:block;font-size:16.5px;line-height:20px;letter-spacing:.5px}
  .arch__contact{position:absolute;left:50px;top:402px}

  .contact__name{font-size:26px;font-weight:600;color:var(--navy);letter-spacing:.5px;line-height:32px}
  .contact__row{display:flex;align-items:center;gap:10px;color:var(--tan);font-size:14.5px;line-height:20px;letter-spacing:.3px}
  .contact__row--phone{color:var(--orange);font-size:22px;line-height:28px}
  .contact__row--indent{padding-left:26px}
  .icon{width:14px;height:14px;flex:none;fill:var(--maroon)}

  /* Horizontal card set A — front */
  .card--a-front{left:660px;top:38px}
  .card--a-front .contact{position:absolute;left:28px;top:26px}
  .card--a-front .contact__name{font-size:20px;line-height:24px}
  .card--a-front .contact__row{font-size:10.5px;line-height:15px;gap:7px}
  .card--a-front .contact__row--phone{font-size:17px;line-height:21px}
  .card--a-front .icon{width:10px;height:10px}
  .lockup{position:absolute;display:flex;align-items:center;gap:10px;color:var(--navy);font-weight:600}
  .lockup__square{background:var(--navy);flex:none}
  .lockup__text .brand-main{display:block;line-height:1}
  .lockup__text .brand-sub{display:block;line-height:1.2}
  .card--a-front .lockup{right:24px;bottom:26px}
  .card--a-front .lockup__square{width:48px;height:48px}
  .card--a-front .brand-main{font-size:32px}
  .card--a-front .brand-sub{font-size:13px}

  /* Horizontal card set A — back */
  .card--a-back{left:660px;top:270px}
  .quad{position:absolute;width:50%;height:50%}
  .quad--tl{left:0;top:0;background:var(--maroon)}
  .quad--tr{right:0;top:0;background:var(--tan)}
  .quad--bl{left:0;bottom:0;background:var(--orange)}
  .quad--br{right:0;bottom:0;background:var(--navy)}
  .back__mark{position:absolute;left:140px;top:58px;width:100px;height:100px;background:var(--paper)}

  /* Horizontal card set B — back */
  .card--b-back{left:660px;top:502px}
  .bar{position:absolute}
  .card--b-back .bar{left:88px;top:0;width:110px;height:12px;background:var(--maroon)}
  .card--b-back .rule{position:absolute;left:60px;right:60px;height:1px;background:var(--tan)}
  .card--b-back .rule--top{top:74px}
  .card--b-back .rule--bottom{top:142px}
  .card--b-back .lockup{left:0;right:0;top:84px;justify-content:center}
  .card--b-back .lockup__square{width:48px;height:48px}
  .card--b-back .brand-main{font-size:32px}
  .card--b-back .brand-sub{font-size:13px}

  /* Horizontal card set B — front */
  .card--b-front{left:660px;top:734px}
  .card--b-front .bar--top{right:90px;top:0;width:130px;height:12px;background:var(--tan)}
  .card--b-front .bar--bottom{left:120px;bottom:0;width:150px;height:14px;background:var(--orange)}
  .card--b-front .front__mark{position:absolute;left:34px;top:50px;width:84px;height:84px;background:var(--navy)}
  .card--b-front .contact{position:absolute;left:134px;top:46px}
  .card--b-front .contact__name{font-size:19px;line-height:23px}
  .card--b-front .contact__row{font-size:10px;line-height:15px;gap:6px;color:var(--navy)}
  .card--b-front .contact__row--phone{font-size:15px;line-height:19px}
  .card--b-front .icon{width:9px;height:9px}
</style>
</head>
<body>

<svg width="0" height="0" style="position:absolute" aria-hidden="true">
  <defs>
    <symbol id="i-phone" viewBox="0 0 16 16"><path d="M2 5c0-2 2-3 6-3s6 1 6 3v1h-3V5H5v1H2zM4 7h8l2 6H2z"/></symbol>
    <symbol id="i-mail" viewBox="0 0 16 16"><path d="M1 3h14v10H1zM2.5 4.5v1l5.5 4 5.5-4v-1L8 8.5z"/></symbol>
    <symbol id="i-globe" viewBox="0 0 16 16"><path d="M8 1a7 7 0 1 0 0 14A7 7 0 0 0 8 1zm0 1.5c.8 0 1.8 1.8 2 4.5H6c.2-2.7 1.2-4.5 2-4.5zM2.6 7h2c0-1.6.4-3 .9-4a5.6 5.6 0 0 0-2.9 4zm8.8 0h2a5.6 5.6 0 0 0-2.9-4c.5 1 .9 2.4.9 4zM2.6 9a5.6 5.6 0 0 0 2.9 4c-.5-1-.9-2.4-.9-4zm3.4 0c.2 2.7 1.2 4.5 2 4.5s1.8-1.8 2-4.5zm5.4 0c0 1.6-.4 3-.9 4a5.6 5.6 0 0 0 2.9-4z"/></symbol>
    <symbol id="i-home" viewBox="0 0 16 16"><path d="M8 1l7 7h-2v7H9v-4H7v4H3V8H1z"/></symbol>
  </defs>
</svg>

<!-- Vertical arch card -->
<section class="card card--arch">
  <div class="arch__mark" role="img" aria-label="Marlow Interior Designs mark"></div>
  <h1 class="arch__brand"><span class="brand-main">MARLOW</span><span class="brand-sub">INTERIOR DESIGNS</span></h1>
  <div class="arch__contact contact">
    <p class="contact__name">DANE MARLOW</p>
    <p class="contact__row contact__row--phone"><svg class="icon"><use href="#i-phone"/></svg>913-555-0142</p>
    <p class="contact__row"><svg class="icon"><use href="#i-mail"/></svg>DANE@MARLOWDESIGNS.COM</p>
    <p class="contact__row"><svg class="icon"><use href="#i-globe"/></svg>WWW.MARLOWDESIGNS.COM</p>
    <p class="contact__row"><svg class="icon"><use href="#i-home"/></svg>2210 W LARKSPUR LN</p>
    <p class="contact__row contact__row--indent">FAIRVIEW, KS 66000</p>
  </div>
</section>

<!-- Horizontal card A, front -->
<section class="card card--horizontal card--a-front">
  <div class="contact">
    <p class="contact__name">DANE MARLOW</p>
    <p class="contact__row contact__row--phone"><svg class="icon"><use href="#i-phone"/></svg>913-555-0142</p>
    <p class="contact__row"><svg class="icon"><use href="#i-mail"/></svg>DANE@MARLOWDESIGNS.COM</p>
    <p class="contact__row"><svg class="icon"><use href="#i-globe"/></svg>WWW.MARLOWDESIGNS.COM</p>
    <p class="contact__row"><svg class="icon"><use href="#i-home"/></svg>2210 W LARKSPUR LN • FAIRVIEW, KS 66000</p>
  </div>
  <div class="lockup">
    <div class="lockup__square" role="img" aria-label="Marlow Interior Designs mark"></div>
    <div class="lockup__text"><span class="brand-main">MARLOW</span><span class="brand-sub">INTERIOR DESIGNS</span></div>
  </div>
</section>

<!-- Horizontal card A, back -->
<section class="card card--horizontal card--a-back">
  <div class="quad quad--tl"></div>
  <div class="quad quad--tr"></div>
  <div class="quad quad--bl"></div>
  <div class="quad quad--br"></div>
  <div class="back__mark" role="img" aria-label="Marlow Interior Designs mark"></div>
</section>

<!-- Horizontal card B, back -->
<section class="card card--horizontal card--b-back">
  <div class="bar"></div>
  <div class="rule rule--top"></div>
  <div class="lockup">
    <div class="lockup__square" role="img" aria-label="Marlow Interior Designs mark"></div>
    <div class="lockup__text"><span class="brand-main">MARLOW</span><span class="brand-sub">INTERIOR DESIGNS</span></div>
  </div>
  <div class="rule rule--bottom"></div>
</section>

<!-- Horizontal card B, front -->
<section class="card card--horizontal card--b-front">
  <div class="bar bar--top"></div>
  <div class="front__mark" role="img" aria-label="Marlow Interior Designs mark"></div>
  <div class="contact">
    <p class="contact__name">DANE MARLOW</p>
    <p class="contact__row contact__row--phone"><svg class="icon"><use href="#i-phone"/></svg>913-555-0142</p>
    <p class="contact__row"><svg class="icon"><use href="#i-mail"/></svg>DANE@MARLOWDESIGNS.COM</p>
    <p class="contact__row"><svg class="icon"><use href="#i-globe"/></svg>WWW.MARLOWDESIGNS.COM</p>
    <p class="contact__row"><svg class="icon"><use href="#i-home"/></svg>2210 W LARKSPUR LN • FAIRVIEW, KS 66000</p>
  </div>
  <div class="bar bar--bottom"></div>
</section>

</body>
</html>
```